Sign Shop website

We need a web design for a sign company called Quillby Signs that builds signs for shops such as A Frames, Banners, Tennet Boards, Shop front windows etc...

The existing site is avaliable at www.quillbysigns.com.au

We will need to have a fresh makeover. The new site must have the following:

Photo Galleries (broken down into sections)
Store Locations (currently there are 4 stores)
Online quote form
List of services
About Us Page

We just need to front page designed in photoshop (the inner page is not necessary) We have a team that can code the site up.

The website should have the exact logo. Any person who alters the logo, design will be elimated.

No Twitter, RSS, LinkedIn icons

The main colours are yellow, black, blue, red

Target Market(s)

Any business

Industry/Entity Type

It Company

Requirements
Must have
• jQuery slider banner
Should not have
• Alter the logo in any way

```html
<!DOCTYPE html>
<html lang="en">
<head>
<meta charset="utf-8">
<title>Quillby Signs</title>
<link href="https://fonts.googleapis.com/css2?family=Arimo:wght@400;700&display=swap" rel="stylesheet">
<style>
:root{
  --plum:#a3346f;
  --plum-dark:#8e2a60;
  --hero-top:#a14a86;
  --hero-bottom:#b0447a;
  --yellow:#f5b82a;
  --sky:#1aa6cf;
  --sun:#f7c51f;
  --cream:#fdf3df;
  --ink:#222;
  --grey:#555;
  --rule:#e3c3d4;
  --field:#ececec;
}
*{box-sizing:border-box;margin:0;padding:0}
html,body{width:769px;height:1200px;overflow:hidden}
body{position:relative;background:#fff;font-family:"Arimo",Arial,sans-serif;color:var(--ink)}
.abs{position:absolute}

.site-header{left:0;top:0;width:769px;height:107px;background:linear-gradient(#fff,var(--cream))}
.brand{left:29px;top:20px;height:63px;display:flex;align-items:center;gap:10px}
.brand-mark{width:40px;height:40px;background:var(--yellow)}
.brand-name{font-size:26px;font-weight:700;color:var(--plum)}
.main-nav a{position:absolute;top:45px;font-size:14px;color:var(--ink);text-decoration:none}
.nav-active{left:491px;top:0;width:84px;height:107px;background:linear-gradient(#fff7e6,#f6d89a)}

.hero{left:0;top:107px;width:769px;height:318px;background:linear-gradient(var(--hero-top),var(--hero-bottom))}
.hero-photo{left:27px;top:30px;width:413px;height:288px;background:linear-gradient(#7c3b66,#5a3550)}
.hero-title{left:464px;top:164px;font-size:24px;font-weight:700;color:#fff}
.hero-text{left:464px;top:198px;width:270px;font-size:13.5px;font-weight:700;line-height:1.2;color:#fff}
.hero-btn{left:460px;top:257px;width:73px;height:27px;border-radius:7px;background:var(--yellow);color:#fff;font-size:13px;font-weight:700;display:flex;align-items:center;justify-content:center}

.section-title{font-size:17px;font-weight:700;color:var(--plum);left:27px;width:490px;padding-bottom:5px;border-bottom:1px solid var(--rule)}
.welcome-text{left:27px;top:480px;width:490px;font-size:9.5px;line-height:1.3;color:var(--grey)}

.gallery-tile{width:152px;height:125px}

.store{top:941px;width:111px;height:127px;padding:12px 7px;color:#fff;overflow:hidden}
.store h3{font-size:16px;font-weight:400;line-height:1.2}
.store p{font-size:9px;line-height:1.25;margin-top:8px}
.store-num{position:absolute;right:-4px;bottom:-12px;font-size:96px;font-weight:700;color:rgba(255,255,255,.15)}

.panel{left:560px;width:191px;border:1px solid #ddd}
.panel-head{height:30px;background:linear-gradient(var(--plum),var(--plum-dark));color:#fff;font-size:16px;font-weight:700;padding:6px 10px}
.service{position:absolute;left:11px;width:170px;height:55px}
.service-thumb{position:absolute;left:0;top:0;width:58px;height:46px;background:linear-gradient(#d8b33a,#a23a2a);border:1px solid #888}
.service-text{position:absolute;left:73px;top:0;width:95px;font-size:9.5px;line-height:1.2;color:var(--grey)}
.service-text span{display:block;color:var(--plum);margin-top:2px}

.quote-row{position:absolute;left:12px;width:168px;height:20px}
.quote-row label{position:absolute;left:0;top:4px;font-size:9.5px;color:var(--ink)}
.quote-row .field{position:absolute;left:64px;top:0;width:103px;height:19px;background:var(--field);border:1px solid #ddd}
.field.select{background:#fff;border:1px solid #7a9cc8;font-size:10px;padding:3px 4px}
.select svg{position:absolute;right:2px;top:3px}
.send{left:71px;top:322px;width:56px;height:20px;border-radius:10px;background:var(--plum);color:#fff;font-size:10px;display:flex;align-items:center;justify-content:center}

.site-footer{left:0;top:1121px;width:769px;height:79px;background:var(--plum)}
.copyright{left:33px;top:26px;font-size:9.5px;color:#fff}
.footer-nav a{position:absolute;top:26px;font-size:10px;color:#fff;text-decoration:none}
.footer-nav a.current{color:var(--yellow)}
</style>
</head>
<body>

<header class="abs site-header">
  <div class="abs nav-active"></div>
  <div class="abs brand"><span class="brand-mark"></span><span class="brand-name">Quillby Signs</span></div>
  <nav class="main-nav">
    <a style="left:384px">Home</a>
    <a style="left:440px">About</a>
    <a style="left:500px">Our Servies</a>
    <a style="left:593px">Our Portfolio</a>
    <a style="left:689px">Contact Us</a>
  </nav>
</header>

<section class="abs hero">
  <div class="abs hero-photo" role="img" aria-label="Photo of a smiling business team in suits"></div>
  <h1 class="abs hero-title" style="top:164px">Lorem Ipsum is simply</h1>
  <p class="abs hero-text">Lorem Ipsum is simply dummy text of the printing and typesetting industry. Lorem Ipsum has been the industry's standard</p>
  <div class="abs hero-btn">Read More</div>
</section>

<h2 class="abs section-title" style="top:451px">Welcome to our site</h2>
<p class="abs welcome-text">Lorem Ipsum is simply dummy text of the printing and typesetting industry. Lorem Ipsum has been the industry's standard dummy text ever since the 1500s, when an unknown printer took a galley of type and scrambled it to make a type specimen book. It has survived not only five centuries, but also the leap into electronic typesetting, remaining essentially unchanged. It was popularised in the 1960s with the release of Letraset sheets containing Lorem Ipsum passages, and more recently with desktop publishing software like Aldus PageMaker including versions of Lorem Ipsum.</p>

<h2 class="abs section-title" style="top:574px">Photo Galleries</h2>
<div class="abs gallery-tile" style="left:27px;top:608px;background:linear-gradient(135deg,#1d2a2a,#5d8a3a)" role="img" aria-label="Abstract green and silver 3D artwork"></div>
<div class="abs gallery-tile" style="left:196px;top:608px;background:linear-gradient(135deg,#9aa6ab,#6f7e86)" role="img" aria-label="Grey wall graphic with a large arrow"></div>
<div class="abs gallery-tile" style="left:365px;top:608px;background:linear-gradient(135deg,#d8413a,#c4302c)" role="img" aria-label="Red wall mural with flower shapes"></div>
<div class="abs gallery-tile" style="left:27px;top:747px;background:linear-gradient(135deg,#7aa0c8,#d6b8a6)" role="img" aria-label="Photo of a young man on a blue banner"></div>
<div class="abs gallery-tile" style="left:196px;top:747px;background:linear-gradient(135deg,#e8e8e8,#9a9a9a)" role="img" aria-label="Vehicle with printed signage"></div>
<div class="abs gallery-tile" style="left:365px;top:747px;background:linear-gradient(135deg,#4a4a44,#2a2a28)" role="img" aria-label="Shop front window with lettered signs"></div>

<h2 class="abs section-title" style="top:903px">Store Location</h2>
<div class="abs store" style="left:28px;background:var(--plum)"><h3>Lorem Ipsum is simply</h3><p>Lorem Ipsum is simply dummy text of the printing and typesetting industry.</p><span class="store-num">1</span></div>
<div class="abs store" style="left:155px;background:var(--sky)"><h3>Lorem Ipsum is simply</h3><p>Lorem Ipsum is simply dummy text of the printing and typesetting industry.</p><span class="store-num">2</span></div>
<div class="abs store" style="left:281px;background:var(--sun)"><h3>Lorem Ipsum is simply</h3><p>Lorem Ipsum is simply dummy text of the printing and typesetting industry.</p><span class="store-num">3</span></div>
<div class="abs store" style="left:408px;background:var(--plum)"><h3>Lorem Ipsum is simply</h3><p>Lorem Ipsum is simply dummy text of the printing and typesetting industry.</p><span class="store-num">4</span></div>

<aside class="abs panel services" style="top:445px;height:262px">
  <div class="panel-head">Our Services</div>
  <div class="service" style="top:44px"><div class="service-thumb" role="img" aria-label="Yellow shop sign sample"></div><p class="service-text">Lorem Ipsum is simply dummy text of the printing and type-setting industry.<span>Read More</span></p></div>
  <div class="service" style="top:113px"><div class="service-thumb" role="img" aria-label="Yellow shop sign sample"></div><p class="service-text">Lorem Ipsum is simply dummy text of the printing and type-setting industry.<span>Read More</span></p></div>
  <div class="service" style="top:182px"><div class="service-thumb" role="img" aria-label="Yellow shop sign sample"></div><p class="service-text">Lorem Ipsum is simply dummy text of the printing and type-setting industry.<span>Read More</span></p></div>
</aside>

<aside class="abs panel quote" style="top:723px;height:352px">
  <div class="panel-head">Request a Quote</div>
  <div class="quote-row" style="top:40px"><label>Name:</label><span class="field"></span></div>
  <div class="quote-row" style="top:66px"><label>Company:</label><span class="field"></span></div>
  <div class="quote-row" style="top:91px"><label>Phone:</label><span class="field"></span></div>
  <div class="quote-row" style="top:115px"><label>Email Address:</label><span class="field"></span></div>
  <div class="quote-row" style="top:139px"><label>Suburb:</label><span class="field"></span></div>
  <div class="quote-row" style="top:165px"><label>Store:</label><span class="field select" style="left:52px;width:115px">Northvale<svg width="12" height="12"><rect width="12" height="12" fill="#c9d8ee"/><path d="M3 4l3 4 3-4z" fill="#335"/></svg></span></div>
  <div class="quote-row" style="top:192px"><label>Sign Type:</label><span class="field"></span></div>
  <div class="quote-row" style="top:218px"><label>Material:</label><span class="field"></span></div>
  <div class="quote-row" style="top:243px"><label>Sign Size:</label><span class="field"></span></div>
  <div class="quote-row" style="top:268px"><label>Artwork Required:</label><span class="field select" style="left:82px;width:85px"><svg width="12" height="12"><rect width="12" height="12" fill="#c9d8ee"/><path d="M3 4l3 4 3-4z" fill="#335"/></svg></span></div>
  <div class="quote-row" style="top:294px"><label>Other Information:</label><span class="field" style="left:82px;width:85px"></span></div>
  <div class="abs send">Send</div>
</aside>

<footer class="abs site-footer">
  <p class="abs copyright">Copyright 2013 www.quillbysigns.com.au. All right reserved.</p>
  <nav class="footer-nav">
    <a style="left:468px">Home</a>
    <a style="left:510px">About</a>
    <a class="current" style="left:555px">Our Servies</a>
    <a style="left:624px">Our Portfolio</a>
    <a style="left:697px">Contact Us</a>
  </nav>
</footer>

</body>
</html>
```